Amber Lantern Notes Daily book cover

Design a front cover, back cover and spine for book.

Target Market(s)

everyone

Industry/Entity Type

Psychology

Colors

Designer to choose colors to be used in the design.

Requirements
Must have
• I'm thinking of a plain looking book cover, female hands releasing a butterfly vertically to the sky. Maybe have the word 'Happiness' the same color as the butterfly.
Nice to have
• I'm thinking of female hands releasing a butterfly vertically to the sky.

```html
<!DOCTYPE html>
<html lang="en">
<head>
<meta charset="UTF-8">
<title>Amber Lantern Notes Daily – Book Cover</title>
<link rel="stylesheet" href="https://fonts.googleapis.com/css2?family=Oswald:wght@300;400&family=Montserrat:wght@600&family=Questrial&family=Yellowtail&display=swap">
<style>
  :root {
    --sky-top: #e6cbc3;
    --sky-rose: #f0d2c2;
    --sun: #fff3d6;
    --haze-blue: #b8d2da;
    --mist: #e9efe6;
    --meadow-light: #efe6b4;
    --meadow: #d8c777;
    --meadow-deep: #b9a65a;
    --mountain: rgba(150,150,175,0.45);
    --skin: rgba(236,178,130,0.95);
    --skin-soft: rgba(242,196,156,0);
    --wing: rgba(22,32,38,0.92);
    --wing-teal: rgba(40,150,150,0.55);
    --ink: #111111;
    --script-red: #e3121b;
    --script-edge: #3a0000;
    --code-box: #4f343f;
  }
  * { margin: 0; padding: 0; box-sizing: border-box; }
  html, body { width: 1200px; height: 900px; overflow: hidden; background: #ffffff; }

  .cover-wrap {
    position: relative;
    width: 1200px;
    height: 900px;
    overflow: hidden;
  }

  .scene-backdrop {
    position: absolute;
    inset: 0;
    background:
      radial-gradient(ellipse 260px 40px at 900px 300px, var(--mountain), rgba(150,150,175,0) 100%),
      radial-gradient(ellipse 240px 36px at 120px 225px, var(--mountain), rgba(150,150,175,0) 100%),
      radial-gradient(circle at 870px 265px, var(--sun) 0, rgba(255,240,210,0.85) 50px, rgba(255,230,205,0) 220px),
      radial-gradient(circle at 230px 215px, rgba(255,240,215,0.9) 0, rgba(255,235,210,0) 140px),
      linear-gradient(180deg,
        var(--sky-top) 0%,
        var(--sky-rose) 22%,
        #e3d3cf 33%,
        var(--haze-blue) 47%,
        #cfe0e0 58%,
        var(--mist) 68%,
        var(--meadow-light) 78%,
        var(--meadow) 90%,
        var(--meadow-deep) 100%);
  }

  .photo-area { position: absolute; }
  .hands-front {
    left: 860px; top: 655px; width: 360px; height: 190px;
    background: radial-gradient(ellipse 50% 45% at 55% 45%, var(--skin) 0%, rgba(240,190,145,0.6) 55%, var(--skin-soft) 100%);
  }
  .butterfly-front {
    left: 730px; top: 505px; width: 260px; height: 145px;
    background:
      radial-gradient(ellipse 30% 35% at 62% 40%, var(--wing-teal), rgba(40,150,150,0) 100%),
      radial-gradient(ellipse 48% 42% at 55% 50%, var(--wing) 0%, rgba(22,32,38,0.5) 55%, rgba(22,32,38,0) 100%);
  }
  .hands-back {
    left: -20px; top: 765px; width: 290px; height: 125px;
    background: radial-gradient(ellipse 50% 45% at 50% 50%, var(--skin) 0%, rgba(240,190,145,0.6) 55%, var(--skin-soft) 100%);
  }
  .butterfly-back {
    left: 160px; top: 650px; width: 200px; height: 115px;
    background:
      radial-gradient(ellipse 30% 35% at 40% 40%, var(--wing-teal), rgba(40,150,150,0) 100%),
      radial-gradient(ellipse 48% 42% at 50% 50%, var(--wing) 0%, rgba(22,32,38,0.5) 55%, rgba(22,32,38,0) 100%);
  }

  /* Back cover */
  .back-cover {
    position: absolute;
    left: 88px;
    top: 178px;
    width: 410px;
    text-align: center;
    font-family: "Oswald", sans-serif;
    color: var(--ink);
  }
  .back-heading {
    font-weight: 400;
    font-size: 19px;
    letter-spacing: 0.3px;
    margin-bottom: 4px;
  }
  .back-blurb {
    font-weight: 300;
    font-size: 16.5px;
    line-height: 31.3px;
    text-align: justify;
    text-align-last: center;
  }
  .offer-heading {
    font-weight: 300;
    font-size: 16px;
    margin-top: 24px;
    line-height: 31px;
  }
  .offer-list {
    list-style: none;
    font-weight: 300;
    font-size: 16px;
    line-height: 31.5px;
  }
  .code-box {
    position: absolute;
    left: 369px;
    top: 731px;
    width: 184px;
    height: 117px;
    background: var(--code-box);
  }

  /* Spine */
  .spine {
    position: absolute;
    left: 578px;
    top: 48px;
    width: 42px;
    height: 800px;
    display: flex;
    align-items: center;
    writing-mode: vertical-rl;
    color: var(--ink);
  }
  .spine-author {
    font-family: "Montserrat", sans-serif;
    font-weight: 600;
    font-size: 20px;
    letter-spacing: 8px;
    margin-bottom: 64px;
  }
  .spine-title {
    font-family: "Questrial", sans-serif;
    font-size: 29px;
    letter-spacing: 1.5px;
    white-space: nowrap;
  }
  .spine-title .script {
    font-size: 46px;
    margin-top: 10px;
    letter-spacing: 0;
  }

  /* Front cover */
  .front-cover {
    position: absolute;
    left: 620px;
    top: 0;
    width: 580px;
    text-align: center;
    color: var(--ink);
  }
  .front-author {
    margin-top: 68px;
    font-family: "Montserrat", sans-serif;
    font-weight: 600;
    font-size: 28px;
    letter-spacing: 5px;
    padding-left: 40px;
  }
  .front-title {
    margin-top: 118px;
    font-family: "Questrial", sans-serif;
    font-weight: 400;
    line-height: 1;
  }
  .title-main {
    display: block;
    font-size: 62px;
    padding-left: 40px;
  }
  .title-link {
    display: block;
    font-size: 33px;
    margin-top: 4px;
    padding-left: 55px;
  }
  .script {
    font-family: "Yellowtail", cursive;
    font-weight: 400;
    color: var(--script-red);
    text-shadow:
      1px 1px 0 var(--script-edge),
      -1px -1px 0 var(--script-edge),
      1px -1px 0 var(--script-edge),
      -1px 1px 0 var(--script-edge),
      3px 3px 3px rgba(0,0,0,0.35);
  }
  .title-script {
    display: block;
    font-size: 128px;
    margin-top: -22px;
    padding-left: 30px;
  }
</style>
</head>
<body>
  <main class="cover-wrap">
    <div class="scene-backdrop" role="img" aria-label="Photograph of a soft sunrise over misty mountains and a golden meadow"></div>
    <div class="photo-area butterfly-back" role="img" aria-label="Black and turquoise butterfly taking flight"></div>
    <div class="photo-area hands-back" role="img" aria-label="Open female hands releasing the butterfly"></div>
    <div class="photo-area butterfly-front" role="img" aria-label="Black and turquoise butterfly taking flight"></div>
    <div class="photo-area hands-front" role="img" aria-label="Open female hands releasing the butterfly toward the sky"></div>

    <section class="back-cover">
      <h2 class="back-heading">WELCOME TO AMBER LANTERN NOTES DAILY!</h2>
      <p class="back-blurb">Since 2004, we have been using God's Word to help people break free from mental health challenges. We believe that no matter how difficult your life can be, there are practical steps you can take that will strengthen your faith and liberate you from nagging doubts and self-defeating mindsets. Through these 'Bible-rich' tips, our daily conference calls, and contact with our friendly support volunteers, you will find a new sense of peace and happiness. Let the light of Christ burst through the clouds of despair. Become the amazing person God made you to be!</p>
      <p class="offer-heading">THIS BOOK OFFERS:</p>
      <ul class="offer-list">
        <li>•The 'Happiness Basics' Overview</li>
        <li>• 29 In-Depth Happiness Tips</li>
        <li>• Practical self-Help Tools and more.</li>
      </ul>
    </section>
    <div class="code-box"></div>

    <aside class="spine">
      <span class="spine-author">AUTHOR NAME</span>
      <span class="spine-title">Amber Lantern Notes <span class="script">Daily</span></span>
    </aside>

    <section class="front-cover">
      <p class="front-author">AUTHOR NAME</p>
      <h1 class="front-title">
        <span class="title-main">Amber Lantern</span>
        <span class="title-link">Notes</span>
        <span class="title-script script">Daily</span>
      </h1>
    </section>
  </main>
</body>
</html>
```